Brightwell is a company offering Colon Hydrotherapy (or colonics)

Brightwell offers Colon Hydrotherapy using an innovative FDA approved system from the USA. The system is called the TORVA system. The clinic is based in Whangarei, Northland and is the first business of this kind for Northland.
I used to use a design from the Prontaleaf website - a water symbol. However, I want a design that will convey freshness. I want something new and clean which conveys vitality and revitalisation .... perhaps water or bubbles but which brings across the idea of detoxing (which is what colon hydrotherapy does)
The clinic will only be completed in April so for now I have put my mobile number but once in the clinic this will need to be changed to a landline number ... the email address will also change. Thanks for any ideas you give me,
Updates

Hi. I need the name Brightwell first and foremost as this is the name of the Company Underneath this it has to say Colon Hydrotherapy to let people know what Brightwell is My name underneath that would be Marian Holcombe And all contact details to follow this. Thanks !

Target Market(s)

People who are wanting to "detox" and focusing on their health and wellbeing

Industry/Entity Type

Clinic

Contact Information for Business Card

Brightwell
Colon Hydrotherapy
Marian Holcombe
Unit B, 42c Ferrand Lane, Whangarei

021 0487 3916
brightwellclinic@mailnest.example

Font styles to use
Serif

Colors
cee9f6
33a6d7
86cae6

Requirements
Must have
• Stand out with colour or logo

```html
<!DOCTYPE html>
<html lang="en">
<head>
<meta charset="utf-8">
<title>Brightwell Colon Hydrotherapy – Business Card</title>
<link href="https://fonts.googleapis.com/css2?family=Questrial&family=Mulish:wght@400;700&display=swap" rel="stylesheet">
<style>
  :root {
    --brand-blue: #33a6d7;
    --brand-mid: #86cae6;
    --brand-pale: #cee9f6;
    --card-white: #ffffff;
    --backdrop: #e9ecee;
    --text-white: #ffffff;
  }
  * { margin: 0; padding: 0; box-sizing: border-box; }
  html, body {
    width: 1200px; height: 1000px; overflow: hidden;
    background: var(--backdrop);
  }
  .canvas { position: relative; width: 1200px; height: 1000px; }
  .card {
    position: absolute; left: 265px; width: 666px; height: 397px;
    background: var(--card-white);
    box-shadow: 0 4px 14px rgba(0,0,0,0.12);
    overflow: hidden;
  }
  .card--front { top: 73px; }
  .card--back { top: 532px; }

  .brand { position: absolute; color: var(--brand-blue); font-family: "Questrial", sans-serif; }
  .brand__dot {
    position: absolute; border-radius: 50%;
    background: var(--brand-blue);
  }
  .brand__name { position: absolute; white-space: nowrap; line-height: 1; font-weight: 400; }
  .brand__tagline { position: absolute; white-space: nowrap; line-height: 1; color: var(--brand-blue); }

  .card--front .brand__dot { left: 196px; top: 84px; width: 46px; height: 46px; }
  .card--front .brand__name { left: 258px; top: 84px; font-size: 48px; }
  .card--front .brand__tagline { left: 262px; top: 133px; font-size: 19px; }

  .card--back .brand__dot { left: 92px; top: 150px; width: 78px; height: 78px; }
  .card--back .brand__name { left: 190px; top: 150px; font-size: 80px; }
  .card--back .brand__tagline { left: 214px; top: 232px; font-size: 33px; }

  .band { position: absolute; left: 0; top: 0; width: 666px; height: 397px; }
  .band path { fill: var(--brand-blue); }

  .holder {
    position: absolute; left: 102px; top: 272px;
    font-family: "Mulish", sans-serif; font-weight: 700; font-size: 19px;
    color: var(--text-white);
  }
  .divider { position: absolute; left: 307px; top: 239px; width: 1.5px; height: 103px; background: var(--text-white); }
  .contact {
    position: absolute; left: 328px; top: 244px;
    font-family: "Mulish", sans-serif; font-size: 15.5px; color: var(--text-white); line-height: 22px;
  }
  .contact strong { font-weight: 700; }
  .contact__address { margin-top: 12px; font-weight: 700; }
</style>
</head>
<body>
<div class="canvas">
  <section class="card card--front">
    <div class="brand">
      <span class="brand__dot"></span>
      <span class="brand__name">Brightwell</span>
      <span class="brand__tagline">Colon Hydrotherapy</span>
    </div>
    <svg class="band" viewBox="0 0 666 397" aria-hidden="true">
      <path d="M0 197 Q333 240 666 200 L666 372 Q333 340 0 372 Z"/>
    </svg>
    <div class="holder">Marian Holcombe</div>
    <div class="divider"></div>
    <div class="contact">
      <div><strong>Phone</strong>: 021 0487 3916</div>
      <div><strong>Email:</strong> brightwellclinic@mailnest.example</div>
      <div class="contact__address">Unit B, 42c Ferrand Lane,<br>Whangarei</div>
    </div>
  </section>

  <section class="card card--back">
    <div class="brand">
      <span class="brand__dot"></span>
      <span class="brand__name">Brightwell</span>
      <span class="brand__tagline">Colon Hydrotherapy</span>
    </div>
  </section>
</div>
</body>
</html>
```